Vela Stewardship Business Card design

We need a creative business card design for our hospitality management company
We need the following information:
Our business Logo: Vela Stewardship
Name: Mara Dobrinsky
Phone number: 0458 317 642
Email: mara@velastewardship.com.au
Address: 214/53 Penrose Street, Harbourside 3188
Web: www.velastewardship.com.au
I need the design to be a working file so that I can insert the names and numbers of the other staff members of our business.
The cards need to be 90 x 40mm
Thanks
Industry/Entity Type
Hospitality
Look and feel

```html
<!DOCTYPE html>
<html lang="en">
<head>
<meta charset="utf-8">
<title>Vela Stewardship Business Card</title>
<link rel="stylesheet" href="https://fonts.googleapis.com/css2?family=Roboto+Condensed:wght@700&family=Arimo:wght@400&display=swap">
<style>
  :root {
    --page-bg: #ece9e4;
    --card-ink: #231c33;
    --card-edge: #1a1427;
    --mark-white: #f1f2f6;
    --name-blue: #8d9fdc;
    --detail-white: #e4e4ec;
    --web-blue: #8a9bd6;
  }
  * { box-sizing: border-box; margin: 0; padding: 0; }
  html, body {
    width: 1200px;
    height: 1000px;
    overflow: hidden;
    background: var(--page-bg);
  }
  .sheet {
    width: 1200px;
    height: 1000px;
    display: flex;
    flex-direction: column;
    align-items: center;
    justify-content: center;
    gap: 70px;
  }
  .card {
    position: relative;
    width: 720px;
    height: 320px;
    background: var(--card-ink);
    border: 1px solid var(--card-edge);
    box-shadow: 0 10px 28px rgba(30, 20, 40, 0.22);
  }
  .card-front {
    display: flex;
    align-items: center;
    justify-content: center;
  }
  .brand {
    display: flex;
    flex-direction: column;
    align-items: center;
    gap: 16px;
  }
  .brand-square {
    width: 58px;
    height: 58px;
    border: 6px solid var(--mark-white);
  }
  .brand-name {
    font-family: "Roboto Condensed", sans-serif;
    font-weight: 700;
    font-size: 30px;
    letter-spacing: 0.5px;
    color: var(--mark-white);
    text-transform: uppercase;
  }
  .corner-brand {
    position: absolute;
    top: 26px;
    right: 30px;
    display: flex;
    align-items: center;
    gap: 8px;
  }
  .corner-square {
    width: 26px;
    height: 26px;
    border: 4px solid var(--mark-white);
  }
  .corner-name {
    font-family: "Roboto Condensed", sans-serif;
    font-weight: 700;
    font-size: 13px;
    color: var(--mark-white);
    text-transform: uppercase;
  }
  .contact {
    position: absolute;
    left: 74px;
    top: 96px;
    font-family: "Arimo", sans-serif;
    font-weight: 400;
  }
  .person-name {
    font-size: 24px;
    color: var(--name-blue);
    margin-bottom: 26px;
  }
  .detail {
    font-size: 12px;
    line-height: 15px;
    color: var(--detail-white);
  }
  .detail-group + .detail-group { margin-top: 14px; }
  .web {
    margin-top: 16px;
    font-size: 12px;
    color: var(--web-blue);
  }
</style>
</head>
<body>
<main class="sheet">
  <section class="card card-front" aria-label="Card front">
    <div class="brand">
      <div class="brand-square"></div>
      <div class="brand-name">Vela Stewardship</div>
    </div>
  </section>

  <section class="card card-back" aria-label="Card back">
    <div class="corner-brand">
      <span class="corner-name">Vela Stewardship</span>
      <div class="corner-square"></div>
    </div>
    <div class="contact">
      <p class="person-name">Mara Dobrinsky</p>
      <div class="detail-group">
        <p class="detail">0458 317 642</p>
        <p class="detail">mara@velastewardship.com.au</p>
      </div>
      <div class="detail-group">
        <p class="detail">214/53 Penrose Street,</p>
        <p class="detail">Harbourside 3188</p>
      </div>
      <p class="web">www.velastewardship.com.au</p>
    </div>
  </section>
</main>
</body>
</html>
```